International Trade Consulting Firm Seeks Quality Newsletter Design

Our company provides consulting services to Pinnacle 300 type companies. We compete with the largest consulting companies in the world. However, we have the highest level of expertise in the industry and need to look the most professional and high end. We have very relevant and important information to provide our customers about their compliance and projects. We will have the winning design coded to be an e-newsletter, so it needs to be one page. We want to keep our company colors and logo design in the newsletter, they are attached. We DO NOT want it to look like a mini-version of our website. We want a fresh look to this marketing piece. Newsletter will need to include title, possible sub-heading, space for a feature story, 2 other stories included, and space on either the left or right for short cuts, links or highlights of other articles. Contents/'In this issue' section, about us or branding area, section for relevant links, etc...
Target Market(s)
Pinnacle 300 companies, High-level management
Industry/Entity Type
Marketing

```html
<!DOCTYPE html>
<html lang="en">
<head>
<meta charset="utf-8">
<title>Meridian Trade Partners Newsletter</title>
<link rel="stylesheet" href="https://fonts.googleapis.com/css2?family=Open+Sans:ital,wght@0,300;0,400;0,600;0,700;1,700&display=swap">
<style>
:root{
  --bg-top:#2b6ca5;
  --bg-mid:#102a4f;
  --paper:#ffffff;
  --frame:#ececec;
  --ink:#444444;
  --ink-soft:#666666;
  --ink-muted:#7a7a7a;
  --black:#000000;
  --slate:#252a33;
  --gray-band:#efefef;
  --placeholder:#ebebeb;
  --brand-green:#4caf3a;
  --orange:#f5a300;
  --link-blue:#7fb6ee;
  --social:#3b64a8;
}
*{box-sizing:border-box;margin:0;padding:0}
html,body{width:824px;height:1200px;overflow:hidden}
body{
  position:relative;
  font-family:"Open Sans",Arial,sans-serif;
  color:var(--ink);
  background:linear-gradient(180deg,var(--bg-top) 0%,#1d4a80 30%,var(--bg-mid) 55%,#1d4a80 80%,var(--bg-top) 100%);
}
.abs{position:absolute}
.notice{left:0;width:824px;text-align:center;color:#e8eef6;font-size:8.5px;line-height:11px}
.notice a{color:var(--link-blue);text-decoration:none}
.sheet{left:152px;top:67px;width:520px;height:1090px;background:var(--paper)}

.masthead{left:171px;top:85px;width:483px;height:41px;background:var(--black);color:#fff}
.masthead .brand{position:absolute;left:12px;top:6px;font-size:24px;font-weight:700;color:var(--brand-green);letter-spacing:3px;line-height:28px}
.masthead .date{position:absolute;left:241px;top:16px;font-size:8.5px}
.masthead .phone{position:absolute;left:306px;top:8px;font-size:19px;font-weight:400}
.masthead .social{position:absolute;left:440px;top:13px;display:flex;gap:3px}
.masthead .social span{width:12px;height:12px;background:var(--social);display:block}

.hero{left:171px;top:127px;width:483px;height:193px;border:1px solid var(--frame)}
.hero .visual{position:absolute;left:7px;top:7px;width:468px;height:177px;
  background:radial-gradient(ellipse at 50% 30%,#8fd2f5 0%,#2f8fd0 40%,#0e4e93 100%)}
.hero .title{position:absolute;left:159px;top:93px;width:316px;height:66px;background:rgba(25,38,55,.78);color:#fff;
  font-size:19px;line-height:23px;padding:9px 0 0 22px;font-weight:400}

.card{border:3px solid var(--frame);background:var(--paper)}
.feature{left:171px;top:330px;width:303px;height:232px}
.feature h2{position:absolute;left:12px;top:17px;font-size:13px;font-weight:400;color:var(--ink)}
.placeholder{position:absolute;background:var(--placeholder);color:#fff;font-size:11px;display:flex;align-items:flex-end;justify-content:center;padding-bottom:12px}
.feature .placeholder{left:13px;top:42px;width:146px;height:160px;padding-bottom:34px}
.feature .copy{position:absolute;left:173px;top:45px;width:112px;font-size:8.6px;line-height:11.5px;color:var(--ink-soft)}
.feature .copy p+p{margin-top:11px}

.story{top:572px;width:143px;height:233px}
.story.one{left:171px}
.story.two{left:329px}
.story h3{position:absolute;left:12px;top:9px;width:125px;font-size:13px;font-weight:400;line-height:14.5px;color:var(--ink)}
.story .placeholder{left:12px;top:48px;width:120px;height:85px;padding-bottom:2px}
.story p{position:absolute;left:12px;top:144px;width:124px;font-size:8px;line-height:10.5px;color:var(--ink-soft)}

.sidebar{left:484px;top:330px;width:167px;height:475px}
.sidebar .band{position:absolute;left:-3px;width:167px;background:var(--slate);color:#fff;font-style:italic;font-weight:700;font-size:14px;padding-left:16px}
.sidebar .band.articles{top:-3px;height:32px;line-height:30px}
.sidebar .band.video{top:252px;height:31px;line-height:31px;padding-left:18px}
.sidebar ul{list-style:none;position:absolute;left:13px;top:60px;width:145px}
.sidebar li{display:flex;gap:9px;font-size:10.5px;line-height:13.5px;color:var(--ink-muted);margin-bottom:15px}
.sidebar li svg{flex:none;margin-top:0}
.sidebar .clip{position:absolute;left:8px;top:295px;width:146px;height:122px;
  background:linear-gradient(180deg,#8c8778 0%,#5e5b52 55%,#3b4a4a 100%)}
.sidebar .clip svg{position:absolute;left:58px;top:46px}
.sidebar .cta{position:absolute;left:0;top:425px;width:161px;text-align:center;color:var(--orange);font-size:13px;line-height:15px}

.issue{left:171px;top:814px;width:482px;height:198px;background:var(--gray-band)}
.issue .label{position:absolute;left:13px;top:38px;width:147px;height:123px;background:var(--slate);color:#fff;
  font-weight:300;font-size:35px;line-height:33px;letter-spacing:-2.5px;text-align:center;padding-top:28px}
.issue ul{list-style:none;position:absolute;left:181px;top:44px;width:290px}
.issue li{display:flex;gap:13px;font-size:8.6px;line-height:11.7px;color:var(--ink-soft);margin-bottom:14px}
.issue li:nth-child(2){margin-bottom:12px}
.issue li svg{flex:none}

.footer{left:171px;top:1020px;width:482px;height:116px}
.footer .col{position:absolute;top:0;height:110px}
.footer .sender{left:0;width:143px;text-align:center;font-size:8px;color:#444;padding-top:27px}
.footer .sender .brand{margin:9px auto 0;width:93px;height:40px;background:var(--black);color:var(--brand-green);font-size:20px;font-weight:700;letter-spacing:3px;line-height:40px}
.footer .rule{position:absolute;top:6px;width:1px;height:100px;background:var(--frame)}
.footer .visit{left:172px;width:110px;font-size:8.6px;color:#333;padding-top:24px}
.footer .visit ul{list-style:none;margin-top:9px}
.footer .visit li{display:flex;align-items:center;gap:5px;margin-bottom:6px;text-decoration:underline;font-size:8px}
.footer .visit li span{width:10px;height:10px;background:var(--social);display:block}
.footer .visit li:last-child span{background:#c0392b}
.footer .legal{left:277px;width:190px;font-size:8px;line-height:10.8px;color:var(--ink-muted);padding-top:24px}
.footer .legal a{color:var(--orange);text-decoration:underline}
.footer .legal p+p{margin-top:11px}
</style>
</head>
<body>
<svg width="0" height="0" style="position:absolute">
  <defs>
    <symbol id="arrow-circle" viewBox="0 0 20 20">
      <circle cx="10" cy="10" r="8.5" fill="none" stroke="#222" stroke-width="1.4"/>
      <path d="M8 5.5 L12.5 10 L8 14.5" fill="none" stroke="#222" stroke-width="2"/>
    </symbol>
  </defs>
</svg>

<p class="abs notice" style="top:14px">Some contents of this email may not display and / or behave properly.<br>Learn more…</p>
<p class="abs notice" style="top:47px">If you are unable to see the message below, click <a href="#">here</a> to view</p>

<div class="abs sheet"></div>

<header class="abs masthead">
  <div class="brand">MTP</div>
  <div class="date">July 23, 2014</div>
  <div class="phone">555.014.2290</div>
  <div class="social"><span></span><span></span></div>
</header>

<section class="abs hero">
  <div class="visual" role="img" aria-label="Glowing blue world map with network lines"></div>
  <h1 class="title">Meridian Trade Partners<br>Newsletter - 04/14</h1>
</section>

<article class="abs card feature">
  <h2>LOREM IPSUM DOLOR SIT AMET</h2>
  <div class="placeholder" role="img" aria-label="Feature story image">IMAGE</div>
  <div class="copy">
    <p>Lorem ipsum dolor sit amet, consectetur adipis-icing elit, sed do eiusmod tempor incididunt ut labore et dolore magna aliqua.</p>
    <p>velit esse cillum dolore eu fugiat nulla pariatur. Excepteur sint occaecat cupidatat non proident, sunt in culpa qui officia deserunt mollit anim id est laborum</p>
  </div>
</article>

<article class="abs card story one">
  <h3>Lorem ipsum dolor sit amet</h3>
  <div class="placeholder" role="img" aria-label="Story image">IMAGE</div>
  <p>velit esse cillum dolore eu fugiat nulla pariatur. Excepteur sint occaecat cupidatat non proident, sunt in culpa qui officia deserunt mollit anim id est laborum</p>
</article>

<article class="abs card story two">
  <h3>Lorem ipsum dolor sit amet</h3>
  <div class="placeholder" role="img" aria-label="Story image">IMAGE</div>
  <p>velit esse cillum dolore eu fugiat nulla pariatur. Excepteur sint occaecat cupidatat non proident, sunt in culpa qui officia deserunt mollit anim id est laborum</p>
</article>

<aside class="abs card sidebar">
  <div class="band articles">Other articles</div>
  <ul>
    <li><svg width="16" height="16"><use href="#arrow-circle"/></svg>Lorem ipsum dolor sit amet, consectetur adipisicing elit</li>
    <li><svg width="16" height="16"><use href="#arrow-circle"/></svg>sed do eiusmod tempor incididunt ut labore et dolore magna aliqua.</li>
    <li><svg width="16" height="16"><use href="#arrow-circle"/></svg>Lorem ipsum dolor sit amet, consectetur adipisicing elit</li>
  </ul>
  <div class="band video">Latest Video</div>
  <div class="clip" role="img" aria-label="Video still of a business meeting around a glass table">
    <svg width="30" height="30" viewBox="0 0 30 30"><circle cx="15" cy="15" r="14" fill="rgba(255,255,255,.35)" stroke="#fff" stroke-width="1.5"/><path d="M12 9 L21 15 L12 21Z" fill="#fff"/></svg>
  </div>
  <div class="cta">View our Company<br>profile media</div>
</aside>

<section class="abs issue">
  <div class="label">IN THIS<br>ISSUE</div>
  <ul>
    <li><svg width="22" height="22"><use href="#arrow-circle"/></svg>Lorem ipsum dolor sit amet, consectetur adipisicing elit, sed do eiusmod tempor incididunt ut labore et dolore magna aliqua.</li>
    <li><svg width="22" height="22"><use href="#arrow-circle"/></svg>Lorem ipsum dolor sit amet, consectetur adipisicing elit, sed do eiusmod tempor</li>
    <li><svg width="22" height="22"><use href="#arrow-circle"/></svg>Lorem ipsum dolor sit amet, consectetur adipisicing elit, sed do eiusmod tempor</li>
  </ul>
</section>

<footer class="abs card footer">
  <div class="col sender">This message was sent by<div class="brand">MTP</div></div>
  <div class="rule" style="left:174px"></div>
  <div class="col visit" style="left:213px">Visit us at:
    <ul>
      <li><span></span>Linkbook</li>
      <li><span></span>Chirper</li>
      <li><span></span>ViewTube</li>
    </ul>
  </div>
  <div class="rule" style="left:322px"></div>
  <div class="col legal" style="left:346px;width:125px">
    <p>You are receiving this email because you subscribed for our newsletter. To stop receiv-ing it please <a href="#">Unsubscribe here.</a></p>
    <p>Having trouble reading this email? <a href="#">View it in your browser.</a></p>
  </div>
</footer>
</body>
</html>
```